After tattoo calming solution

The label has to be modern, along the same lines as skin care brand “Dew Harbor.” It has to reflect the solutions natural effectiveness and simplicity. The label cannot be over fussy, and must be a little bit clinical, as it really does work. The colours should reflect that the solution calms the skin.

We use a 100ml spray bottle.

Target Market(s)

Anyone with a new tattoo or piercing

Industry/Entity Type

Skincare

Requirements
Must have
• Must reflect its natural calming but still remain a little clinical
Should not have
• It must not look like other flowery tattoo cream solutions.

```html
<!DOCTYPE html>
<html lang="en">
<head>
<meta charset="utf-8">
<title>After Tattoo &amp; Piercing – Label</title>
<link href="https://fonts.googleapis.com/css2?family=Marcellus&family=Questrial&display=swap" rel="stylesheet">
<style>
  :root {
    --ink-navy: #0f3f7c;
    --ink-black: #111111;
    --label-white: #ffffff;
    --backdrop: #f1f2f3;
    --rule-grey: #8a8a8a;
  }
  html, body {
    margin: 0;
    padding: 0;
    width: 769px;
    height: 1200px;
    overflow: hidden;
    background: var(--backdrop);
  }
  .label {
    position: absolute;
    left: 98px;
    top: 55px;
    width: 572px;
    height: 1090px;
    background: var(--label-white);
    box-shadow: 0 0 0 1px #e4e4e4;
  }
  .label > * { position: absolute; margin: 0; }
  .headline {
    left: 48px;
    font-family: "Marcellus", serif;
    font-weight: 400;
    color: var(--ink-navy);
    font-size: 80px;
    line-height: 1;
    letter-spacing: 1px;
    white-space: nowrap;
  }
  .headline--expert { top: 66px; }
  .headline--repair { top: 168px; }
  .subhead {
    left: 50px;
    top: 268px;
    font-family: "Marcellus", serif;
    color: var(--ink-navy);
    font-size: 50px;
    line-height: 62px;
    letter-spacing: 4px;
  }
  .divider {
    left: 28px;
    top: 422px;
    width: 530px;
    height: 2px;
    background: linear-gradient(90deg, transparent, var(--rule-grey) 12%, var(--rule-grey) 88%, transparent);
  }
  .benefits {
    left: 48px;
    top: 438px;
    font-family: "Marcellus", serif;
    color: var(--ink-black);
    font-size: 30px;
    line-height: 45px;
    letter-spacing: 2px;
  }
  .product-name {
    left: 42px;
    top: 618px;
    font-family: "Questrial", sans-serif;
    color: var(--ink-black);
    font-size: 108px;
    line-height: 117px;
    letter-spacing: 1px;
  }
  .brand-mark {
    left: 402px;
    top: 620px;
    width: 100px;
    height: 100px;
  }
  .volume {
    top: 1024px;
    font-family: "Marcellus", serif;
    color: var(--ink-black);
    font-size: 30px;
    letter-spacing: 2px;
  }
  .volume--metric { left: 48px; }
  .volume--imperial { right: 30px; font-size: 28px; }
</style>
</head>
<body>
  <main class="label">
    <h1 class="headline headline--expert">EXPERT</h1>
    <p class="headline headline--repair">SKIN REPAIR</p>
    <p class="subhead">for new tattoos<br>&amp; piercings</p>
    <div class="divider"></div>
    <p class="benefits">reduces inflammation,<br>irritation and encourages<br>natural skin healing</p>
    <p class="product-name">AFTER<br>TATTOO &amp;<br>PIERCING</p>
    <svg class="brand-mark" viewBox="0 0 100 100" role="img" aria-label="Veyla">
      <circle cx="50" cy="50" r="46" fill="none" stroke="#111111" stroke-width="3"/>
      <text x="50" y="56" text-anchor="middle" font-family="Marcellus, serif" font-size="17" letter-spacing="1" fill="#0f3f7c">Veyla</text>
    </svg>
    <p class="volume volume--metric">100ml ℮</p>
    <p class="volume volume--imperial">3.4 fl oz</p>
  </main>
</body>
</html>
```